I need some Graphic Design Menu card for my Quick Service Restaurant

Hi,
I need a graphic design menu with Combos for my Quick service restaurant serving Momos, Wraps, Burgers, Sandwiches, Fried Chicken etc...
Name of my restaurant is "TANGO DEPOT" and I already have a logo for it.

Expecting the Newly designed Menu with nice images with the Al-Carte items and the combos in it.

Theme of my restaurant is with "Red & Green" representing the Veg and Non-veg segment.

Target audiences are Gen Y & Z, Kids, College students and young adults.

Attached are Logo and Existing Menu card image file.

UPDATE: Also attached the sample menu which can be used to frame the new menu design

```html
<!DOCTYPE html>
<html lang="en">
<head>
<meta charset="utf-8">
<title>Tango Depot Menu</title>
<link rel="stylesheet" href="https://fonts.googleapis.com/css2?family=Oswald:wght@500;600;700&family=Roboto+Condensed:ital,wght@0,400;0,700;1,400&display=swap">
<style>
:root{
  --green:#5cae2a;
  --green-light:#9bd04a;
  --green-dark:#2f7f1e;
  --green-pale:#dff0c4;
  --red:#e31b23;
  --gold-dark:#c39433;
  --gold-light:#f3e2a4;
  --ink:#141414;
  --blue:#1d3f9a;
  --paper:#ffffff;
}
*{margin:0;padding:0;box-sizing:border-box}
html,body{width:1200px;height:848px;overflow:hidden;background:#fff}
body{position:relative;font-family:"Roboto Condensed",Arial,sans-serif;color:var(--ink)}
.sheet{position:absolute;top:29px;width:550px;height:780px;background:var(--paper);overflow:hidden;box-shadow:0 0 6px rgba(0,0,0,.18)}
.sheet--menu{left:27px}
.sheet--combos{left:620px}
.sheet > *{position:absolute}
.top-band,.bottom-band{left:0;width:550px}
.top-band{top:0;height:60px}
.bottom-band{bottom:0;height:110px}
.brand{top:30px;width:200px;text-align:center}
.brand-name{font-family:"Oswald",sans-serif;font-weight:700;font-size:34px;line-height:1;color:var(--red);display:flex;align-items:center;justify-content:center;gap:8px}
.brand-dot{width:14px;height:14px;border-radius:50%;background:var(--green)}
.brand-tag{font-size:13px;color:var(--blue);margin-top:6px;font-style:italic}
.tab{height:26px;padding-left:12px;display:flex;align-items:center;font-family:"Oswald",sans-serif;font-weight:600;font-size:15px;color:#fff;letter-spacing:.3px;background:linear-gradient(90deg,var(--gold-dark),var(--gold-light));}
.tab::after{content:"";position:absolute;right:-10px;top:-4px;width:12px;height:34px;background:#e9e9e9;clip-path:polygon(0 12%,100% 0,100% 100%,0 88%)}
.list{font-size:13px;line-height:13px;white-space:nowrap}
.list--tight{line-height:12.6px;font-size:12.4px}
.list small{font-size:9px}
.photo{border-radius:10px}
.pin{width:54px;height:74px}
.footer-text{left:220px;bottom:10px;color:#fff;font-size:12.5px;line-height:17px}
.footer-title{font-family:"Oswald",sans-serif;font-weight:600;font-size:19px;color:var(--red);letter-spacing:.6px;line-height:22px;margin-bottom:3px}
.combos-title{left:17px;top:80px;font-family:"Oswald",sans-serif;font-weight:700;font-size:32px;color:var(--green);letter-spacing:1px}
.bar{height:22px;padding-left:10px;border-radius:11px;display:flex;align-items:center;font-family:"Oswald",sans-serif;font-weight:600;font-size:14.5px;color:var(--green-dark);background:linear-gradient(90deg,var(--green-light),var(--green-pale) 70%,#fff)}
.badge{width:48px;height:48px;border-radius:50%;background:var(--red);border:2px solid #fff;box-shadow:0 0 0 1px #ddd;color:#fff;text-align:center;font-family:"Oswald",sans-serif;font-weight:600;font-size:17px;line-height:16px;padding-top:7px}
.badge span{display:block;font-size:9px;line-height:10px;font-family:"Roboto Condensed",sans-serif;font-weight:400}
.combo-text{font-size:13px;line-height:16px;text-align:center;white-space:nowrap;transform:translateX(-50%)}
.combo-note{color:var(--green);font-size:12px}
</style>
</head>
<body>

<!-- A LA CARTE SHEET -->
<section class="sheet sheet--menu">
  <svg class="top-band" viewBox="0 0 550 60" preserveAspectRatio="none" aria-hidden="true">
    <path d="M0 0H550V20C420 10 300 40 160 34 90 31 40 22 0 30Z" fill="var(--green)"/>
    <path d="M0 30C40 22 90 31 160 34 300 40 420 10 550 20V26C420 16 300 46 160 40 90 37 40 28 0 36Z" fill="var(--green-light)"/>
  </svg>

  <div class="brand" style="left:300px"><div class="brand-name"><span class="brand-dot"></span>TANGO DEPOT</div><div class="brand-tag">Grab It, You'll Love It !!!</div></div>

  <div class="tab" style="left:131px;top:64px;width:150px">KAATI ROLLS</div>
  <div class="photo" role="img" aria-label="Photo of stuffed kaati roll wraps" style="left:7px;top:91px;width:120px;height:107px;background:radial-gradient(circle at 50% 50%,#d9a26a,#b9683a 60%,#f4efe6 90%)"></div>
  <div class="list" style="left:140px;top:95px">
    <div>Aloo Tikki &nbsp;Rs.40/-</div><div>Mixed Veg &nbsp;Rs.40/-</div><div>Paneer Roll &nbsp;Rs.50/-</div><div>Spicy Baby Corn Roll &nbsp;Rs.50/-</div><div>Egg Roll &nbsp;Rs.40/-</div><div>Spicy Chicken Roll &nbsp;Rs.50/-</div><div>Egg with Chicken Roll &nbsp;Rs.60/-</div>
  </div>

  <div class="tab" style="left:360px;top:151px;width:133px">MOMOS</div>
  <div class="list" style="left:364px;top:183px">
    <div>Veg Momo Steam Rs.40/-</div><div>Veg Momo Fried Rs.50/-</div><div>Chicken Momo Steam Rs.50/-</div><div>Chicken Momo Fried Rs.60/-</div>
  </div>

  <div class="tab" style="left:131px;top:197px;width:150px">SANDWICH</div>
  <div class="photo" role="img" aria-label="Photo of grilled sandwiches on a plate" style="left:7px;top:220px;width:120px;height:87px;background:radial-gradient(ellipse at 50% 55%,#e8cf9a,#a9774a 60%,#fff 92%)"></div>
  <div class="list" style="left:140px;top:227px">
    <div>Veg Sandwich &nbsp;Rs.40/-</div><div>Cheese Grilled Sandwich &nbsp;Rs.40/-</div><div>Corn Sandwich &nbsp;Rs.40/-</div><div>PaneerGriled Sandwich &nbsp;Rs.50/-</div><div>Mushroom Sandwich &nbsp;Rs.50/-</div><div>ChickenSandwich &nbsp;Rs.50/-</div>
  </div>

  <div class="tab" style="left:360px;top:251px;width:133px">BIRIYANI</div>
  <div class="list" style="left:364px;top:287px"><div>Chicken Biriyani &nbsp;Rs.100/-</div></div>

  <div class="photo" role="img" aria-label="Photo of a pepperoni pizza on a board" style="left:354px;top:307px;width:180px;height:92px;border-radius:50%;background:radial-gradient(circle,#d9462b,#b8331d 45%,#e7b45a 62%,#8a5a2b 75%,#fff 76%)"></div>

  <div class="tab" style="left:11px;top:320px;width:136px">ADD ON</div>
  <div class="list" style="left:20px;top:357px"><div>Egg &nbsp;Rs.10/-</div><div>Cheese &nbsp;Rs.10/-</div><div>Mayonnaise Rs.10/-</div></div>

  <div class="tab" style="left:194px;top:320px;width:140px">BEVERAGES</div>
  <div class="photo" role="img" aria-label="Photo of a glass of cola with ice" style="left:171px;top:352px;width:47px;height:67px;border-radius:6px;background:linear-gradient(180deg,#e8e8e8,#5a1a12 30%,#2a0a06)"></div>
  <div class="list" style="left:226px;top:356px"><div>Cola &nbsp;Rs.20/-</div><div>Orange Fizz &nbsp;Rs.20/-</div><div>Lime Soda &nbsp;Rs.20/-</div><div>Thunder Cola &nbsp;Rs.20/-</div></div>

  <div class="tab" style="left:360px;top:400px;width:133px">PIZZA</div>
  <div class="list" style="left:364px;top:431px">
    <div>Veg Pizza &nbsp;Rs.80/-</div><div>Paneer Pizza &nbsp;Rs.90/-</div><div>Mushroom Pizza &nbsp;Rs.90/-</div><div>Baby Corn Pizza &nbsp;Rs.90/-</div><div>Sweet Corn Pizza &nbsp;Rs.90/-</div><div>Chicken Pizza &nbsp;Rs.100/-</div>
  </div>

  <div class="tab" style="left:11px;top:420px;width:136px">FRIES</div>
  <div class="list list--tight" style="left:20px;top:450px">
    <div>Cutlet &nbsp;Rs.40/-</div><div>French Fries<small>(Regular)</small> Rs.40/-</div><div>French Fries<small>(Large)</small> Rs.60/-</div><div>Smileys &nbsp;Rs.40/-</div><div>Potato Pops &nbsp;Rs.40/-</div><div>Chicken Popcorn &nbsp;Rs.60/-</div><div>Chicken Garlic Fingers &nbsp;Rs.60/-</div><div>Chicken Nuggets &nbsp;Rs.60/-</div><div>Chicken Lolly Pop &nbsp;Rs.80/-</div><div>Chicken Wings <small>(3 pcs)</small> Rs.50/-</div><div>Chicken Wings <small>(3 pcs)</small> Rs.580/-</div>
  </div>

  <div class="tab" style="left:194px;top:460px;width:140px">ICE CREAM</div>
  <div class="list" style="left:200px;top:492px"><div>Kulfi &nbsp;Rs.35/-</div></div>
  <div class="photo" role="img" aria-label="Photo of french fries on a white plate" style="left:200px;top:510px;width:147px;height:62px;border-radius:50%;background:radial-gradient(ellipse,#f4c542,#e9a722 50%,#fff 72%)"></div>

  <div class="tab" style="left:360px;top:526px;width:133px">BURGER</div>
  <div class="list" style="left:364px;top:557px">
    <div>Veg Classic Burger &nbsp;Rs.50/-</div><div>Aloo Tikki Burger &nbsp;Rs.50/-</div><div>Herb Chili Burger &nbsp;Rs.50/-</div><div>Veg Momo Burger &nbsp;Rs.50/-</div><div>Chicken Momo Burger Rs.50/-</div><div>Chicken Burger &nbsp;Rs.50/-</div>
  </div>

  <div class="tab" style="left:194px;top:598px;width:140px">FRIED CHICKEN</div>
  <div class="list" style="left:206px;top:630px"><div>1 Pcs &nbsp;Rs.50/-</div><div>2 Pcs &nbsp;Rs.95/-</div><div>4 Pcs &nbsp;Rs.180/-</div><div>8 Pcs &nbsp;Rs.350/-</div></div>

  <div class="photo" role="img" aria-label="Photo of crispy fried chicken pieces with dip" style="left:7px;top:598px;width:180px;height:100px;background:radial-gradient(ellipse at 50% 45%,#e19a3c,#b56418 55%,#fff 80%)"></div>
  <div class="photo" role="img" aria-label="Photo of two burgers" style="left:373px;top:638px;width:147px;height:52px;background:radial-gradient(ellipse at 28% 50%,#c98a3e 0 35%,transparent 37%),radial-gradient(ellipse at 72% 50%,#c98a3e 0 35%,transparent 37%)"></div>

  <svg class="bottom-band" viewBox="0 0 550 110" preserveAspectRatio="none" aria-hidden="true">
    <path d="M0 40C150 10 330 20 550 45V110H0Z" fill="var(--green-light)"/>
    <path d="M0 48C150 20 330 28 550 52V110H0Z" fill="var(--green)"/>
  </svg>
  <svg class="pin" viewBox="0 0 54 74" style="left:160px;bottom:8px" aria-hidden="true">
    <path d="M27 72C14 52 3 42 3 27A24 24 0 0 1 51 27C51 42 40 52 27 72Z" fill="#fff" stroke="var(--red)" stroke-width="3"/>
    <text x="27" y="25" text-anchor="middle" font-family="Oswald,sans-serif" font-weight="600" font-size="10" fill="var(--red)">BEST</text>
    <text x="27" y="37" text-anchor="middle" font-family="Oswald,sans-serif" font-weight="600" font-size="10" fill="var(--red)">PRICE</text>
  </svg>
  <div class="footer-text">
    <div class="footer-title">TANGO DEPOT RESTAURANT</div>
    <div>Lakeview Nagar, Next to St. Mary Church</div>
    <div>Branch: Grand Market, Millbrook</div>
    <div>Connect us at: 900 555 0147</div>
  </div>
</section>

<!-- COMBOS SHEET -->
<section class="sheet sheet--combos">
  <svg class="top-band" viewBox="0 0 550 60" preserveAspectRatio="none" aria-hidden="true">
    <path d="M0 0H550V20C420 10 300 40 160 34 90 31 40 22 0 30Z" fill="var(--green)"/>
    <path d="M0 30C40 22 90 31 160 34 300 40 420 10 550 20V26C420 16 300 46 160 40 90 37 40 28 0 36Z" fill="var(--green-light)"/>
  </svg>
  <div class="brand" style="left:305px"><div class="brand-name"><span class="brand-dot"></span>TANGO DEPOT</div><div class="brand-tag">Grab It, You'll Love It !!!</div></div>

  <div class="combos-title">COMBOS</div>

  <div class="bar" style="left:17px;top:127px;width:250px">1. YUMMY BURGER COMBOS</div>
  <div class="photo" role="img" aria-label="Photo of burger, fries and cola" style="left:84px;top:157px;width:123px;height:75px;background:linear-gradient(90deg,#5a1a12 0 25%,#c98a3e 25% 70%,#f0b52e 70%)"></div>
  <div class="badge" style="left:205px;top:160px"><span>Rs.</span>100/-</div>
  <div class="combo-text" style="left:143px;top:240px">Burger + French Fries + Cool Drinks<div class="combo-note">Upgrade to Large french Fries @ Rs.20/- extra</div></div>

  <div class="photo" role="img" aria-label="Photo of fried chicken, cola and burger" style="left:327px;top:157px;width:125px;height:75px;background:linear-gradient(90deg,#c47a2a 0 35%,#5a1a12 35% 60%,#c98a3e 60%)"></div>
  <div class="badge" style="left:465px;top:157px"><span>Rs.</span>100/-</div>
  <div class="combo-text" style="left:413px;top:240px">Burger + Fried Chicken (1 Pc)<br>+ Cool Drinks</div>

  <div class="bar" style="left:17px;top:281px;width:250px">2. CHICKEN COMBO BIRIYANI</div>
  <div class="photo" role="img" aria-label="Photo of biriyani bowl, cola and fried chicken" style="left:30px;top:330px;width:115px;height:90px;background:radial-gradient(ellipse at 40% 60%,#f1e0b0,#d9b36a 55%,#fff 78%)"></div>
  <div class="badge" style="left:130px;top:322px"><span>Rs.</span>160/-</div>
  <div class="photo" role="img" aria-label="Photo of biriyani bowl, cola and hot wings" style="left:207px;top:330px;width:115px;height:90px;background:radial-gradient(ellipse at 40% 60%,#f1e0b0,#d9b36a 55%,#fff 78%)"></div>
  <div class="badge" style="left:293px;top:322px"><span>Rs.</span>150/-</div>
  <div class="photo" role="img" aria-label="Photo of two biriyani bowls and hot wings" style="left:375px;top:330px;width:120px;height:90px;background:radial-gradient(ellipse at 45% 60%,#f1e0b0,#d9b36a 55%,#fff 78%)"></div>
  <div class="badge" style="left:462px;top:322px"><span>Rs.</span>250/-</div>
  <div class="combo-text" style="left:89px;top:431px">Biriyani + Fried Chicken<br>+ Cool Drinks</div>
  <div class="combo-text" style="left:267px;top:431px">Biriyani + 2pcs Hot Wings<br>+ Cool Drinks</div>
  <div class="combo-text" style="left:453px;top:431px">Biriyani (2 nos)<br>+ 4 pcs Hot Wings</div>

  <div class="bar" style="left:17px;top:466px;width:236px">3. PIZZA FAMILY VALUE COMBO</div>
  <div class="bar" style="left:320px;top:466px;width:167px">4. KIDS VALUE MEAL</div>
  <div class="photo" role="img" aria-label="Photo of two pizzas and a bottle of cola" style="left:33px;top:500px;width:175px;height:100px;background:radial-gradient(circle at 30% 55%,#d9462b,#e7b45a 45%,transparent 48%),radial-gradient(circle at 72% 40%,#d9462b,#e7b45a 40%,transparent 43%)"></div>
  <div class="badge" style="left:193px;top:508px"><span>Rs.</span>200/-</div>
  <div class="combo-text" style="left:127px;top:618px">Any 2 pizzas + 2 Nos Cool Drinks</div>
  <div class="photo" role="img" aria-label="Photo of a child with a drink pack and fries" style="left:327px;top:500px;width:133px;height:105px;background:linear-gradient(180deg,#f3e6d8,#9fc6e8 60%,#f0b52e)"></div>
  <div class="badge" style="left:457px;top:511px"><span>Rs.</span>60/-</div>
  <div class="combo-text" style="left:413px;top:618px">French Fries/Smileys(2 pcs) +<br>Chicken Popcorn(5 pcs) + Mango Sip</div>

  <div class="bar" style="left:17px;top:640px;width:190px">5. SANDWICH COMBO</div>
  <div class="list" style="left:31px;top:670px;font-size:13px">Any Sandwich + French Fries + Cool Drinks</div>
  <div class="badge" style="left:287px;top:650px"><span>Rs.</span>100/-</div>

  <svg class="bottom-band" viewBox="0 0 550 110" preserveAspectRatio="none" aria-hidden="true">
    <path d="M0 40C150 10 330 20 550 45V110H0Z" fill="var(--green-light)"/>
    <path d="M0 48C150 20 330 28 550 52V110H0Z" fill="var(--green)"/>
  </svg>
  <svg class="pin" viewBox="0 0 54 74" style="left:160px;bottom:8px" aria-hidden="true">
    <path d="M27 72C14 52 3 42 3 27A24 24 0 0 1 51 27C51 42 40 52 27 72Z" fill="#fff" stroke="var(--red)" stroke-width="3"/>
    <text x="27" y="25" text-anchor="middle" font-family="Oswald,sans-serif" font-weight="600" font-size="10" fill="var(--red)">BEST</text>
    <text x="27" y="37" text-anchor="middle" font-family="Oswald,sans-serif" font-weight="600" font-size="10" fill="var(--red)">PRICE</text>
  </svg>
  <div class="footer-text">
    <div class="footer-title">TANGO DEPOT RESTAURANT</div>
    <div>Lakeview Nagar, Next to St. Mary Church</div>
    <div>Branch: Grand Market, Millbrook</div>
    <div>Connect us at: 900 555 0147</div>
  </div>
</section>

</body>
</html>
```